하늘마루 건축사사무소 종합건설(주) 브로셔/리플렛 디자인 의뢰 사례 — 브로셔/리플렛 당선작
일반/기타 업종의 하늘마루 건축사사무소 종합건설(주)가 모음디자인에서 브로셔/리플렛 디자인을 의뢰한 실제 사례입니다. 총 5개 시안 중 1위작이 선정됐으며, 진행 기간 10일, 의뢰 비용 40만 원, 고객 평점 5점을 기록했습니다.
브랜드 소개
하늘마루은 개발/시행,디자인,설계,시공,분양을 진행하는 종합건축회사입니다.
현재 분양을 진행하고있는 건물(솔바람레지던스)에 대해 홍보 리플렛을 제작하려고 합니다.
브로셔/리플렛 디자인 관련 자주 묻는 질문
브로셔/리플렛 디자인 비용은 얼마인가요?
모음디자인에서 브로셔/리플렛 디자인 의뢰 비용은 프로젝트 규모에 따라 다르며, 이 사례의 경우 40만 원으로 진행됐습니다.
브로셔/리플렛 디자인 제작 기간은 얼마나 걸리나요?

```html
<!DOCTYPE html>
<html lang="ko">
<head>
<meta charset="utf-8">
<title>솔바람레지던스 가람1 분양임대 리플렛</title>
<link href="https://fonts.googleapis.com/css2?family=Noto+Sans+KR:wght@400;500;700;900&family=Josefin+Sans:wght@300;400;600&display=swap" rel="stylesheet">
<style>
:root{
  --green:#2e5a47;
  --green-dark:#244a3a;
  --beige:#d8cb9f;
  --beige-light:#e6dcb8;
  --paper:#ffffff;
  --bg:#ececec;
  --ink:#2b2b2b;
  --muted:#7a7a7a;
  --photo-sky:#a9b7c2;
}
*{box-sizing:border-box;margin:0;padding:0}
html,body{width:1200px;height:1200px;overflow:hidden}
body{background:var(--bg);font-family:"Noto Sans KR",sans-serif;color:var(--ink);position:relative}

/* cover */
.cover{position:absolute;left:60px;top:270px;width:450px;height:660px;background:var(--beige);overflow:hidden}
.cover-top{position:absolute;left:0;top:0;width:100%;height:225px;background:var(--green)}
.brand{position:absolute;left:28px;top:22px;display:flex;align-items:center;gap:6px;color:#fff;font-size:12px;font-weight:700;letter-spacing:1px}
.brand-dot{width:9px;height:9px;border-radius:50%;background:var(--beige)}
.title{position:absolute;left:28px;top:84px;color:var(--beige);display:flex;align-items:center;gap:8px}
.title-main{font-family:"Josefin Sans",sans-serif;font-weight:300;font-size:46px;letter-spacing:4px;line-height:1}
.title-sub{font-family:"Josefin Sans",sans-serif;font-size:9.5px;line-height:1.3;letter-spacing:1px;color:#fff;white-space:nowrap}
.building-photo{position:absolute;left:244px;top:36px;width:196px;height:196px;border-radius:50%;background:linear-gradient(180deg,var(--photo-sky),#d6dbe0 55%,#8c9298);border:4px solid var(--green)}
.pitch{position:absolute;left:28px;top:254px;font-size:12.5px;line-height:1.5;font-weight:500;color:var(--green-dark)}
.pitch p+p{margin-top:8px}
.offer{position:absolute;left:28px;top:408px;color:var(--green-dark)}
.offer-lead{font-size:15px;font-weight:700}
.offer-main{font-size:40px;font-weight:900;letter-spacing:2px;line-height:1.1}
.contact{position:absolute;left:28px;top:484px;font-size:10px;line-height:1.55;color:var(--green-dark)}
.contact strong{font-weight:700}
.badges{position:absolute;left:330px;top:492px;display:flex;gap:10px}
.badge{width:34px;height:34px;border-radius:50%;border:2px solid var(--green)}
.skyline{position:absolute;left:0;bottom:0;width:100%;height:100px;background:linear-gradient(180deg,#3a6753,var(--green-dark))}

/* inner spread */
.spread{position:absolute;left:540px;top:270px;width:600px;height:660px;display:flex;background:var(--paper)}
.panel{position:relative;width:300px;height:100%}
.panel-left{border-right:1px solid #e2e2e2}
.map{position:absolute;left:14px;top:14px;width:160px;height:200px;background:linear-gradient(135deg,#f4f4f4,#e3e3e3)}
.legend{position:absolute;left:184px;top:18px;width:104px;font-size:8px;line-height:1.45;color:var(--muted)}
.legend-intro{color:var(--ink);font-size:8.5px;margin-bottom:8px}
.legend dt{color:var(--green);font-weight:700;margin-top:6px}
.legend dt::before{content:"";display:inline-block;width:5px;height:5px;border-radius:50%;background:var(--green);margin-right:4px;vertical-align:1px}
.nearby{position:absolute;left:0;top:232px;width:300px;height:230px}
.arc{position:absolute;width:74px;height:74px;border-radius:50%;background:var(--beige-light)}
.spot{position:absolute;width:62px;height:62px;border-radius:50%;background:linear-gradient(160deg,#9a9a9a,#3e3e3e)}
.spot-label{position:absolute;font-size:7px;color:var(--muted);width:80px;text-align:center}
.says{position:absolute;left:0;bottom:0;width:100%;height:170px;background:var(--paper);padding:20px 22px}
.says h3{font-family:"Josefin Sans",sans-serif;font-weight:600;font-size:13px;letter-spacing:1px;color:var(--green)}
.says p{margin-top:10px;font-size:8.5px;line-height:1.6;color:var(--muted)}
.says-rule{width:40px;height:2px;background:var(--green);margin-top:8px}

.point{position:absolute;left:0;width:300px;height:106px;display:flex;border-bottom:1px solid #ececec}
.point-text{width:172px;padding:10px 10px 0 14px}
.point-num{font-size:7.5px;color:var(--green);font-weight:700}
.point h4{font-size:11px;line-height:1.35;color:var(--green);font-weight:700;margin-top:3px}
.point p{font-size:7.5px;line-height:1.5;color:var(--muted);margin-top:5px}
.point-photo{width:128px;height:100%}
.point.band .point-text{background:var(--green)}
.point.band .point-num,.point.band h4{color:#fff}
.point.band p{color:#d9e3dd}
</style>
</head>
<body>

<section class="cover" aria-label="리플렛 표지">
  <div class="cover-top">
    <div class="brand"><span class="brand-dot"></span>하늘마루</div>
    <div class="title">
      <span class="title-main">SOL</span>
      <span class="title-sub">SOLBARAM<br>RESIDENCE<br>GARAM I</span>
    </div>
  </div>
  <div class="building-photo" role="img" aria-label="솔바람레지던스 가람1 건물 외관 사진"></div>

  <div class="pitch">
    <p>강남 가람동의 중심!<br>솔내, 가람역 더블역세권!<br>복층스타일의 젊은 감각의 고급주거!<br>신투자금 대비 기대수익률 5% 이상</p>
    <p>최고의 학군 가람동 학원가의 중심!<br>가람동 아파트 전세 대비 월세 부담 감소<br>가람동 아파트 평균 시세 대비 가격 경쟁력</p>
  </div>

  <div class="offer">
    <div class="offer-lead">가람동 512-7 총 32세대 상가</div>
    <div class="offer-main">분/양/임/대</div>
  </div>

  <div class="contact">
    <strong>분양문의</strong> 02 555 0147<br>
    <strong>하늘마루</strong> 홈페이지 www.haneulmaru.co.kr<br>
    <strong>분양홈페이지</strong> www.solbaram-garam.kr<br>
    누리검색 솔바람레지던스
  </div>
  <div class="badges">
    <span class="badge"></span><span class="badge"></span>
  </div>

  <div class="skyline" role="img" aria-label="건물과 도시 실루엣 일러스트"></div>
</section>

<section class="spread" aria-label="리플렛 내지">
  <div class="panel panel-left">
    <div class="map" role="img" aria-label="솔바람레지던스 주변 위치 약도"></div>
    <div class="legend">
      <p class="legend-intro">솔바람레지던스 가람1은 다양한 생활 편의시설과 교육 인프라를 누립니다.</p>
      <dl>
        <dt>교육시설</dt><dd>가람초, 가람중, 학원가</dd>
        <dt>대형상권</dt><dd>백화점, 마트, 상가 밀집</dd>
        <dt>공원</dt><dd>가람근린공원 인접</dd>
        <dt>병원</dt><dd>종합병원 차량 5분</dd>
        <dt>교통시설</dt><dd>가람역, 솔내역 도보권</dd>
      </dl>
    </div>

    <div class="nearby">
      <span class="arc" style="left:22px;top:22px"></span>
      <span class="spot" role="img" aria-label="인근 학원가 사진" style="left:28px;top:28px"></span>
      <span class="spot-label" style="left:19px;top:8px">학원가</span>
      <span class="arc" style="left:113px;top:60px"></span>
      <span class="spot" role="img" aria-label="인근 공원 사진" style="left:119px;top:66px"></span>
      <span class="spot-label" style="left:110px;top:46px">근린공원</span>
      <span class="arc" style="left:204px;top:22px"></span>
      <span class="spot" role="img" aria-label="인근 백화점 사진" style="left:210px;top:28px"></span>
      <span class="spot-label" style="left:201px;top:8px">백화점</span>
      <span class="arc" style="left:60px;top:120px"></span>
      <span class="spot" role="img" aria-label="인근 마트 사진" style="left:66px;top:126px"></span>
      <span class="spot-label" style="left:57px;top:196px">대형마트</span>
      <span class="arc" style="left:166px;top:120px"></span>
      <span class="spot" role="img" aria-label="인근 역사 사진" style="left:172px;top:126px"></span>
      <span class="spot-label" style="left:163px;top:196px">가람역</span>
    </div>

    <div class="says">
      <h3>SOLBARAM RESIDENCE GARAM SAYS...</h3>
      <div class="says-rule"></div>
      <p>필요한 것은 다 있고, 불필요한 것은 없는 곳에서 살아보세요. 역세권 입지와 학군, 생활 편의시설을 모두 갖추었습니다. 최신 설계와 고급 마감으로 완성한 공간에서 새로운 일상을 누려 보세요.</p>
    </div>
  </div>

  <div class="panel panel-right">
    <div class="point" style="top:0">
      <div class="point-text">
        <div class="point-num">1 Point</div>
        <h4>2.5M의 높은 천장고와 시원하게 탁 트인 전망</h4>
        <p>높은 천장고로 개방감을 더하고 넓은 창으로 도심 전망을 누립니다.</p>
      </div>
      <div class="point-photo" role="img" aria-label="창밖 도심 전망 사진" style="background:linear-gradient(180deg,#b9c8d3,#8e9aa2)"></div>
    </div>
    <div class="point" style="top:106px">
      <div class="point-text">
        <div class="point-num">2 Point</div>
        <h4>자유로운 공간구획, 층간소음 방지 및 지진에 강한 기둥식 구조</h4>
        <p>기둥식 구조로 공간 변경이 쉽고 소음과 진동에 강합니다.</p>
      </div>
      <div class="point-photo" role="img" aria-label="세대 평면 구조 도면" style="background:linear-gradient(180deg,#f2f2f2,#dfe6e2)"></div>
    </div>
    <div class="point band" style="top:212px">
      <div class="point-text">
        <div class="point-num">3 Point</div>
        <h4>넉넉한 자주식 지하주차장</h4>
        <p>세대별 여유 있는 주차 공간을 자주식으로 마련했습니다.</p>
      </div>
      <div class="point-photo" role="img" aria-label="지하주차장 사진" style="background:linear-gradient(180deg,#d8dadb,#9fa3a5)"></div>
    </div>
    <div class="point" style="top:318px">
      <div class="point-text">
        <div class="point-num">4 Point</div>
        <h4>변화하는 라이프스타일에 맞춘 대면형 주방</h4>
        <p>가족과 마주하며 요리할 수 있는 대면형 주방을 적용했습니다.</p>
      </div>
      <div class="point-photo" role="img" aria-label="대면형 주방 인테리어 사진" style="background:linear-gradient(180deg,#ece6dc,#c7bba9)"></div>
    </div>
    <div class="point band" style="top:424px">
      <div class="point-text">
        <div class="point-num">5 Point</div>
        <h4>주거와 상가의 독립된 진입부</h4>
        <p>주거 출입구를 상가와 분리해 사생활과 보안을 지킵니다.</p>
      </div>
      <div class="point-photo" role="img" aria-label="건물 진입부 외관 사진" style="background:linear-gradient(180deg,#c9d0d4,#8d969b)"></div>
    </div>
    <div class="point" style="top:530px;height:130px;border-bottom:0">
      <div class="point-text">
        <div class="point-num">6 Point</div>
        <h4>모든 방에 시스템에어컨 설치</h4>
        <p>모든 방에 천장형 시스템에어컨을 설치해 쾌적하고 깔끔합니다.</p>
      </div>
      <div class="point-photo" role="img" aria-label="천장형 시스템에어컨 사진" style="background:linear-gradient(180deg,#f4f4f4,#d4d6d7)"></div>
    </div>
  </div>
</section>

</body>
</html>
```